11 x 11 Flyer Design for Social Media - Reverse Mortgages

62 or older?

A Reverse Mortgage
could be
Your Road to Financial Freedom

* No Monthly Payments
* No Income Requirements
* No Credit Score Requirements
* No Loss of Ownership

Receive cash by lump sum, monthly installments or a line of credit!!

Call us today for a Free Consultation!!
(800) 471-2965

Bluegate Financial Services, Inc.
NMLS #318760
www.bluegatehome.com

```html
<!DOCTYPE html>
<html lang="en">
<head>
<meta charset="utf-8">
<title>Reverse Mortgage Flyer – Bluegate Financial Services</title>
<link rel="stylesheet" href="https://fonts.googleapis.com/css2?family=Montserrat:wght@300;400;500;600;700;800&family=Arimo:wght@400&display=swap">
<style>
  :root {
    --blue: #0462a8;
    --blue-dark: #0a4f8c;
    --gold: #b8a42a;
    --gold-bright: #d4bd1f;
    --grey-panel: #e6e7e9;
    --grey-text: #5e6063;
    --ink: #1d1d1f;
    --white: #ffffff;
    --sky-top: #ffffff;
    --sky-bottom: #b9cde0;
  }
  * { box-sizing: border-box; margin: 0; padding: 0; }
  html, body { width: 1200px; height: 1200px; overflow: hidden; background: var(--white); }
  .flyer {
    position: relative; width: 1200px; height: 1200px; overflow: hidden;
    background: linear-gradient(160deg, var(--sky-top) 35%, var(--sky-bottom) 100%);
    font-family: "Montserrat", sans-serif;
  }
  .hero-photo {
    position: absolute; left: 560px; top: 0; width: 640px; height: 733px;
    background: radial-gradient(ellipse at 60% 55%, #efe6dc 0%, #d9cfc6 35%, #b7c8d8 75%, #c7d6e4 100%);
  }
  .brand {
    position: absolute; left: 56px; top: 130px; display: flex; align-items: center; gap: 16px;
    color: var(--blue); font-weight: 700; font-size: 30px; line-height: 1.1;
  }
  .brand-dot { width: 56px; height: 56px; border-radius: 50%; background: var(--gold); flex: none; }
  .shapes { position: absolute; left: 0; top: 0; width: 1200px; height: 1200px; }
  .headline-age {
    position: absolute; left: 52px; top: 338px; color: var(--white);
    font-weight: 700; font-size: 98px; letter-spacing: -2px; line-height: 1;
  }
  .headline-age .small { font-weight: 400; font-size: 56px; letter-spacing: 0; }
  .tagline-band {
    position: absolute; left: 68px; top: 477px; height: 60px; line-height: 60px;
    color: var(--white); font-family: "Arimo", sans-serif; font-size: 38px;
  }
  .headline-road {
    position: absolute; left: 52px; top: 562px; color: var(--white);
    font-weight: 300; font-size: 60px; line-height: 1;
  }
  .headline-freedom {
    position: absolute; left: 52px; top: 632px; color: var(--white);
    font-weight: 700; font-size: 59px; line-height: 1;
  }
  .feature {
    position: absolute; top: 787px; width: 190px; margin-left: -95px; text-align: center;
    color: var(--ink); font-size: 20px; font-weight: 500; line-height: 1.22; letter-spacing: 0.3px;
  }
  .feature svg { display: block; margin: 0 auto 12px; }
  .side-photo {
    position: absolute; left: 803px; top: 766px; width: 364px; height: 197px;
    clip-path: polygon(0 0, 100% 0, 100% 100%, 13% 100%);
    background: linear-gradient(120deg, #8fa5a0 0%, #d6c7b2 45%, #a3b8d4 75%, #2c3e5a 100%);
  }
  .cash-line {
    position: absolute; left: 50px; top: 974px; height: 55px; line-height: 55px;
    color: var(--white); font-weight: 600; font-size: 29.5px; letter-spacing: 0.6px;
  }
  .cta {
    position: absolute; left: 55px; top: 1067px; color: var(--white);
    font-family: "Arimo", sans-serif; font-size: 30px;
  }
  .phone {
    position: absolute; left: 55px; top: 1100px; display: flex; align-items: center; gap: 30px;
    color: var(--white); font-weight: 500; font-size: 54px; line-height: 60px;
  }
  .company {
    position: absolute; left: 709px; top: 1046px; color: var(--blue);
    font-weight: 600; font-size: 27px; letter-spacing: 0.4px;
  }
  .license {
    position: absolute; left: 709px; top: 1086px; color: var(--grey-text);
    font-weight: 500; font-size: 26px; letter-spacing: 0.6px;
  }
  .website {
    position: absolute; left: 709px; top: 1129px; height: 48px; line-height: 48px;
    color: var(--white); font-weight: 700; font-size: 31px; letter-spacing: 1.2px;
  }
</style>
</head>
<body>
<main class="flyer">
  <div class="hero-photo" role="img" aria-label="Smiling senior couple embracing on a sunny beach"></div>

  <div class="brand"><span class="brand-dot"></span><span>Bluegate<br>Financial Services, Inc.</span></div>

  <svg class="shapes" viewBox="0 0 1200 1200" aria-hidden="true">
    <!-- headline panel -->
    <polygon points="0,307 597,307 764,747 0,747" fill="var(--blue)"/>
    <polygon points="663,472 690,472 771,733 1200,733 1200,740 764,740" fill="var(--gold)"/>
    <polygon points="52,477 636,477 656,537 52,537" fill="var(--gold)"/>
    <!-- divider lines -->
    <rect x="0" y="752" width="1183" height="3" fill="var(--gold)"/>
    <rect x="1181" y="752" width="3" height="219" fill="var(--gold)"/>
    <!-- features strip -->
    <polygon points="0,762 788,762 853,967 0,967" fill="var(--grey-panel)"/>
    <rect x="202" y="814" width="2" height="117" fill="var(--ink)"/>
    <rect x="398" y="814" width="2" height="117" fill="var(--ink)"/>
    <rect x="619" y="814" width="2" height="117" fill="var(--ink)"/>
    <!-- cash band -->
    <rect x="0" y="974" width="1200" height="55" fill="var(--gold)"/>
    <!-- contact panels -->
    <polygon points="0,1047 609,1047 682,1200 0,1200" fill="var(--blue)"/>
    <polygon points="650,1129 1200,1129 1200,1177 672,1177" fill="var(--gold)"/>
  </svg>

  <h1 class="headline-age">62 <span class="small">or</span> older?</h1>
  <p class="tagline-band">A Reverse Mortgage could be</p>
  <h2 class="headline-road">Your Road to</h2>
  <h2 class="headline-freedom">Financial Freedom</h2>

  <div class="feature" style="left:114px">
    <svg width="76" height="76" viewBox="0 0 76 76"><circle cx="38" cy="38" r="34" fill="none" stroke="var(--blue)" stroke-width="6"/><rect x="18" y="27" width="40" height="22" rx="2" fill="none" stroke="var(--gold)" stroke-width="4"/><circle cx="38" cy="38" r="6" fill="none" stroke="var(--gold)" stroke-width="3"/><line x1="16" y1="60" x2="60" y2="16" stroke="var(--gold)" stroke-width="5"/></svg>
    No Monthly<br>Payments
  </div>
  <div class="feature" style="left:301px">
    <svg width="76" height="76" viewBox="0 0 76 76"><circle cx="38" cy="38" r="34" fill="none" stroke="var(--blue)" stroke-width="6"/><circle cx="42" cy="28" r="9" fill="none" stroke="var(--gold)" stroke-width="3"/><path d="M16 50 L30 44 L48 48 L58 42" fill="none" stroke="var(--gold)" stroke-width="4"/><line x1="16" y1="60" x2="60" y2="16" stroke="var(--gold)" stroke-width="5"/></svg>
    No Income<br>Requirements
  </div>
  <div class="feature" style="left:507px">
    <svg width="76" height="76" viewBox="0 0 76 76"><circle cx="38" cy="38" r="34" fill="none" stroke="var(--blue)" stroke-width="6"/><rect x="17" y="25" width="42" height="27" rx="3" fill="none" stroke="var(--gold)" stroke-width="4"/><line x1="17" y1="33" x2="59" y2="33" stroke="var(--gold)" stroke-width="4"/><line x1="16" y1="60" x2="60" y2="16" stroke="var(--gold)" stroke-width="5"/></svg>
    No Credit Score<br>Requirements
  </div>
  <div class="feature" style="left:709px">
    <svg width="76" height="76" viewBox="0 0 76 76"><circle cx="38" cy="38" r="34" fill="none" stroke="var(--blue)" stroke-width="6"/><circle cx="34" cy="25" r="7" fill="none" stroke="var(--gold)" stroke-width="3"/><path d="M22 54 C22 40 46 40 46 54" fill="none" stroke="var(--gold)" stroke-width="3"/><circle cx="48" cy="40" r="6" fill="none" stroke="var(--gold)" stroke-width="3"/><line x1="16" y1="60" x2="60" y2="16" stroke="var(--gold)" stroke-width="5"/></svg>
    No Loss of<br>Ownership
  </div>

  <div class="side-photo" role="img" aria-label="Laughing senior couple riding in a convertible car"></div>

  <p class="cash-line">Receive cash by lump sum, monthly installments or a line of credit!!</p>

  <p class="cta">Call us today for a Free Consultation!!</p>
  <p class="phone">
    <svg width="46" height="46" viewBox="0 0 24 24" aria-hidden="true"><path fill="var(--white)" d="M6.6 10.8a15.1 15.1 0 0 0 6.6 6.6l2.2-2.2a1 1 0 0 1 1-.25 11.4 11.4 0 0 0 3.6.57 1 1 0 0 1 1 1V20a1 1 0 0 1-1 1A17 17 0 0 1 3 4a1 1 0 0 1 1-1h3.5a1 1 0 0 1 1 1c0 1.25.2 2.45.57 3.57a1 1 0 0 1-.25 1z"/></svg>
    <span>(800) 471-2965</span>
  </p>

  <p class="company">Bluegate Financial Services, Inc.</p>
  <p class="license">NMLS #318760</p>
  <p class="website">www.bluegatehome.com</p>
</main>
</body>
</html>
```